Website update for Harbor Broker Ledger & Payroll Services

Our website needs updating
www.harborbrokerledgers.com
Here are some of our latest print pieces to use as a guide?
I have also attached our graphic identity guide which includes the Pantone colors

Target Market(s)

Insurance Agencies

Industry/Entity Type

Accounting

Number of Pages Required

5+ page

```html
<!DOCTYPE html>
<html lang="en">
<head>
<meta charset="utf-8">
<title>Harbor Broker Ledger &amp; Payroll Services</title>
<link href="https://fonts.googleapis.com/css2?family=Open+Sans:wght@400;600;700&family=Great+Vibes&display=swap" rel="stylesheet">
<style>
:root{
  --teal:#1fa99a;
  --teal-light:#d8f1ee;
  --ink:#333a40;
  --muted:#8a9096;
  --band:#eceeef;
  --footer:#55595d;
  --white:#ffffff;
}
*{box-sizing:border-box;margin:0;padding:0}
html,body{width:707px;height:1200px;overflow:hidden;background:var(--white)}
body{font-family:"Open Sans",Arial,sans-serif;color:var(--ink);position:relative}
.abs{position:absolute}

.site-header{position:absolute;left:0;top:0;width:707px;height:62px;background:var(--white)}
.brand{position:absolute;left:22px;top:12px;display:flex;align-items:flex-start;gap:6px;color:var(--teal);font-weight:700}
.brand-mark{width:12px;height:12px;background:var(--teal);margin-top:5px}
.brand-name{font-size:20px;line-height:22px}
.brand-full{font-size:6.5px;line-height:8px;width:90px;margin-top:2px}
.call{position:absolute;right:14px;top:14px;font-size:8px;color:var(--muted);display:flex;align-items:center;gap:4px}
.call strong{color:var(--teal);font-size:9px}
.main-nav{position:absolute;left:283px;top:40px;width:412px;display:flex;justify-content:space-between;font-size:8px;font-weight:600;color:var(--ink)}
.main-nav span{position:relative}
.main-nav .active{color:var(--teal)}
.main-nav .active::before{content:"";position:absolute;left:-8px;right:-8px;top:-6px;height:2px;background:var(--teal)}

.hero{position:absolute;left:0;top:62px;width:707px;height:308px;
  background:linear-gradient(100deg,#c9d3d8 0%,#e4e8ea 40%,#f1ede8 62%,#d7dde0 100%)}
.hero-title{position:absolute;left:46px;top:208px;font-family:"Great Vibes",cursive;font-size:30px;color:var(--white)}
.hero-text{position:absolute;left:48px;top:246px;width:210px;font-size:8px;line-height:11px;color:var(--white)}
.hero-arrows{position:absolute;left:48px;top:292px;display:flex;gap:8px}
.hero-arrows span{width:20px;height:20px;border-radius:50%;background:var(--white);display:flex;align-items:center;justify-content:center}

.welcome-title{position:absolute;left:0;top:452px;width:707px;text-align:center;font-size:26px;font-weight:400}
.welcome-title b{color:var(--teal);font-weight:700}
.welcome-text{position:absolute;left:150px;top:492px;width:407px;text-align:center;font-size:7px;line-height:11px;color:var(--muted)}
.btn{position:absolute;left:313px;top:550px;width:80px;height:20px;background:var(--teal);color:var(--white);font-size:7.5px;display:flex;align-items:center;justify-content:center}

.services{position:absolute;left:0;top:600px;width:707px;height:360px;background:var(--band)}
.section-title{position:absolute;left:0;width:707px;text-align:center;font-size:24px;font-weight:400}
.section-title b{font-weight:700}
.services .section-title{top:20px}
.service{position:absolute;width:150px;text-align:center}
.service-icon{width:76px;height:76px;margin:0 auto;border-radius:50%;border:3px solid var(--teal);background:var(--teal-light)}
.service-label{margin-top:8px;font-size:8.5px;font-weight:700;color:var(--teal);line-height:11px;text-transform:uppercase}

.news .section-title{top:972px}
.news-item{position:absolute;top:1020px;width:270px}
.news-date{position:absolute;left:0;top:0;width:40px;text-align:left}
.news-date .day{font-size:26px;font-weight:700;color:var(--teal);line-height:26px}
.news-date .month{font-size:6px;color:var(--muted)}
.news-body{position:absolute;left:44px;top:2px;width:220px}
.news-body h3{font-size:9px;font-weight:700;text-transform:uppercase}
.news-body p{font-size:7px;line-height:10px;color:var(--muted);margin-top:4px}
.news-body .more{font-size:7px;font-weight:700;color:var(--teal);margin-top:5px}

.site-footer{position:absolute;left:0;top:1118px;width:707px;height:82px}
.footer-url{position:absolute;left:46px;top:26px;font-size:8px;font-weight:600;color:var(--white);text-transform:uppercase}
.footer-phone{position:absolute;left:46px;top:46px;font-size:14px;font-weight:700;color:var(--white)}
.social{position:absolute;left:560px;top:30px;display:flex;gap:4px}
.social span{width:14px;height:14px;border-radius:50%;background:var(--white)}
.copyright{position:absolute;left:540px;top:56px;font-size:6px;color:#d5d8da}
</style>
</head>
<body>

<header class="site-header">
  <div class="brand">
    <span class="brand-mark"></span>
    <div>
      <div class="brand-name">HBLP</div>
      <div class="brand-full">Harbor Broker Ledger &amp; Payroll Services</div>
    </div>
  </div>
  <div class="call">
    <svg width="9" height="9" viewBox="0 0 24 24"><path fill="#1fa99a" d="M6.6 10.8a15 15 0 0 0 6.6 6.6l2.2-2.2a1 1 0 0 1 1-.25 11.4 11.4 0 0 0 3.6.57 1 1 0 0 1 1 1V20a1 1 0 0 1-1 1A17 17 0 0 1 3 4a1 1 0 0 1 1-1h3.5a1 1 0 0 1 1 1c0 1.25.2 2.45.57 3.57a1 1 0 0 1-.25 1z"/></svg>
    CALL US <strong>1800-555-010</strong>
  </div>
  <nav class="main-nav">
    <span class="active">HOME</span><span>|</span><span>ABOUT US</span><span>|</span><span>SERVICES</span><span>|</span><span>BLOG</span><span>|</span><span>NEWS</span><span>|</span><span>CONTACT US</span>
  </nav>
</header>

<section class="hero" role="img" aria-label="Photo of a smiling accountant at a laptop in a bright office with colleagues talking behind her"></section>
<h1 class="hero-title">Insurances do matter</h1>
<p class="hero-text">Clear books and timely reports for agencies that want to grow with confidence.</p>
<div class="hero-arrows">
  <span><svg width="8" height="8" viewBox="0 0 10 10"><path d="M6.5 1.5 3 5l3.5 3.5" stroke="#333a40" stroke-width="1.6" fill="none"/></svg></span>
  <span><svg width="8" height="8" viewBox="0 0 10 10"><path d="M3.5 1.5 7 5 3.5 8.5" stroke="#333a40" stroke-width="1.6" fill="none"/></svg></span>
</div>

<h2 class="welcome-title">Welcome to <b>HBLP</b></h2>
<p class="welcome-text">We handle the accounting behind your insurance agency so your team can focus on clients. From direct bill commissions to payroll, our staff reconciles every statement and keeps your ledger current. Monthly reports arrive on time and in plain language, so you always know where the agency stands.</p>
<div class="btn">Read More</div>

<section class="services">
  <h2 class="section-title">Our <b>SERVICES</b></h2>
  <div class="service" style="left:31px;top:62px"><div class="service-icon" role="img" aria-label="Piggy bank icon"></div><div class="service-label">Record direct bill<br>commission</div></div>
  <div class="service" style="left:208px;top:62px"><div class="service-icon" role="img" aria-label="Banknote icon"></div><div class="service-label">Reconcile &amp; pay agency<br>bill premiums</div></div>
  <div class="service" style="left:361px;top:62px"><div class="service-icon" role="img" aria-label="Ledger sheet icon"></div><div class="service-label">Reconcile general<br>ledger account</div></div>
  <div class="service" style="left:514px;top:62px"><div class="service-icon" role="img" aria-label="Financial report icon"></div><div class="service-label">Prepare &amp;<br>interpret financial</div></div>
  <div class="service" style="left:125px;top:206px"><div class="service-icon" role="img" aria-label="Invoice icon"></div><div class="service-label">Pay vendor<br>invoices</div></div>
  <div class="service" style="left:279px;top:206px"><div class="service-icon" role="img" aria-label="Received stamp icon"></div><div class="service-label">Reconcile customer<br>account receivable</div></div>
  <div class="service" style="left:432px;top:206px"><div class="service-icon" role="img" aria-label="Payroll calculator icon"></div><div class="service-label">Process<br>payroll</div></div>
</section>

<section class="news">
  <h2 class="section-title">Latest <b style="color:var(--teal)">NEWS</b></h2>
  <article class="news-item" style="left:46px">
    <div class="news-date"><div class="day">02</div><div class="month">OCT 2015</div></div>
    <div class="news-body"><h3>Aliquam erat volut</h3><p>New payroll deadlines for the coming quarter and what your agency should prepare now.</p><div class="more">READ MORE</div></div>
  </article>
  <article class="news-item" style="left:372px">
    <div class="news-date"><div class="day">05</div><div class="month">OCT 2015</div></div>
    <div class="news-body"><h3>Aliquam erat volut</h3><p>How monthly reconciliation of agency bill premiums keeps carrier accounts in good order.</p><div class="more">READ MORE</div></div>
  </article>
</section>

<footer class="site-footer">
  <svg class="abs" style="left:0;top:0" width="707" height="82" viewBox="0 0 707 82" preserveAspectRatio="none">
    <defs><linearGradient id="footerShade" x1="0" y1="0" x2="1" y2="0"><stop offset="0" stop-color="#4b4f53"/><stop offset="1" stop-color="#66696c"/></linearGradient></defs>
    <path d="M0 14 Q354 -6 707 14 V82 H0 Z" fill="url(#footerShade)"/>
  </svg>
  <div class="footer-url">www.harborbrokerledgers.com</div>
  <div class="footer-phone">860-555-0148</div>
  <div class="social"><span></span><span></span><span></span><span></span><span></span><span></span></div>
  <div class="copyright">© 2015, HBLP. All Rights Reserved.</div>
</footer>

</body>
</html>
```